Business card

We are looking for a creative person to deigns our company business card.

Target Market(s)

College age student

Industry/Entity Type

Accommodation

Contact Information for Business Card

We want a fun, clean and sophisticated design. It should look good, but more importantly the information should be legible.

Font styles to use
Serif
Sans Serif
Other font styles liked:
• Open Sans ,

Colors
33a6d7

Requirements
Must have
• Must have a young and memorable message. Be legible.
• Our logo on the back on a solid blue , please find color and logo attached
• LodgeBridgely.net on the back.
Nice to have
• I would like to have couple of different fonts on the LodgeBridgely.net on the back of the cards with a solid blue.

```html
<!DOCTYPE html>
<html lang="en">
<head>
<meta charset="utf-8">
<title>LodgeBridgely Business Card</title>
<link href="https://fonts.googleapis.com/css2?family=Open+Sans:wght@400;600&family=Archivo:wght@800&family=Libre+Baskerville&display=swap" rel="stylesheet">
<style>
  :root {
    --backdrop: #2a2a2c;
    --brand-deep: #17628f;
    --brand-band: #155a88;
    --brand-light: #33a6d7;
    --paper: #f7f8f9;
    --ink-white: #ffffff;
    --soft-white: #e9eff4;
  }
  * { margin: 0; padding: 0; box-sizing: border-box; }
  html, body {
    width: 1200px; height: 900px; overflow: hidden;
    background: var(--backdrop);
  }
  .stage {
    position: relative; width: 1200px; height: 900px;
    display: flex; flex-direction: column; align-items: center;
    justify-content: center; gap: 44px;
  }
  .card {
    position: relative; width: 680px; height: 388px;
    overflow: hidden; border-radius: 3px;
    box-shadow: 0 10px 26px rgba(0,0,0,0.45);
  }

  /* Back of card */
  .card-back {
    background: var(--brand-deep);
    display: flex; flex-direction: column; align-items: center; justify-content: center;
  }
  .back-mark {
    display: flex; align-items: center; gap: 14px;
  }
  .back-mark .mark-square {
    width: 26px; height: 26px; background: var(--ink-white);
  }
  .back-mark .wordmark {
    font-family: "Archivo", "Helvetica Neue", Arial, sans-serif;
    font-weight: 800; font-size: 40px; letter-spacing: -0.5px;
    color: var(--ink-white);
  }
  .back-url {
    margin-top: 58px;
    font-family: "Libre Baskerville", Georgia, serif;
    font-size: 15px; letter-spacing: 0.6px; color: var(--soft-white);
  }

  /* Front of card */
  .card-front { background: var(--paper); }
  .front-band {
    position: absolute; inset: 0; width: 100%; height: 100%;
  }
  .front-wordmark {
    position: absolute; left: 58px; top: 108px;
    font-family: "Archivo", "Helvetica Neue", Arial, sans-serif;
    font-weight: 800; font-size: 46px; letter-spacing: -0.5px;
    color: var(--brand-deep);
  }
  .front-emblem {
    position: absolute; right: 92px; top: 42px;
    width: 150px; height: 150px; border-radius: 50%;
    background: var(--brand-light);
    border: 6px solid var(--paper);
  }
  .person {
    position: absolute; left: 58px; top: 262px; color: var(--ink-white);
    font-family: "Open Sans", Arial, sans-serif;
  }
  .person-name { font-size: 30px; font-weight: 600; line-height: 1.1; }
  .person-title { font-size: 20px; font-weight: 400; margin-top: 2px; }
  .person-address {
    margin-top: 18px; font-size: 15px; line-height: 1.5; color: var(--soft-white);
  }
  .contact {
    position: absolute; right: 52px; top: 272px;
    list-style: none; color: var(--ink-white);
    font-family: "Open Sans", Arial, sans-serif; font-size: 16px; line-height: 1.55;
  }
  .contact li { display: flex; align-items: center; gap: 10px; }
  .contact svg { width: 15px; height: 15px; flex: none; }
</style>
</head>
<body>
<main class="stage">

  <section class="card card-back" aria-label="Card back">
    <div class="back-mark">
      <span class="mark-square"></span>
      <span class="wordmark">LodgeBridgely</span>
    </div>
    <p class="back-url">www.LodgeBridgely.net</p>
  </section>

  <section class="card card-front" aria-label="Card front">
    <svg class="front-band" viewBox="0 0 680 388" preserveAspectRatio="none" aria-hidden="true">
      <polygon points="0,240 680,132 680,388 0,388" fill="var(--brand-band)"/>
    </svg>

    <div class="front-wordmark">LodgeBridgely</div>
    <div class="front-emblem"></div>

    <div class="person">
      <p class="person-name">Marcus Wendell</p>
      <p class="person-title">President</p>
      <p class="person-address">Level 2, 19 Harbour Lane<br>Kestonvale, NSW 2041</p>
    </div>

    <ul class="contact">
      <li>
        <svg viewBox="0 0 24 24" aria-hidden="true"><path fill="#fff" d="M6.6 10.8a15.1 15.1 0 0 0 6.6 6.6l2.2-2.2c.3-.3.7-.4 1-.2 1.1.4 2.3.6 3.6.6.6 0 1 .4 1 1V20c0 .6-.4 1-1 1A17 17 0 0 1 3 4c0-.6.4-1 1-1h3.5c.6 0 1 .4 1 1 0 1.3.2 2.5.6 3.6.1.3 0 .7-.2 1z"/></svg>
        412 508 7736
      </li>
      <li>
        <svg viewBox="0 0 24 24" aria-hidden="true"><rect x="2" y="5" width="20" height="14" fill="#fff"/><path d="M2 5l10 8 10-8" fill="none" stroke="var(--brand-band)" stroke-width="2"/></svg>
        info@LodgeBridgely.net
      </li>
      <li>
        <svg viewBox="0 0 24 24" aria-hidden="true"><g fill="none" stroke="#fff" stroke-width="2"><circle cx="12" cy="12" r="9.5"/><ellipse cx="12" cy="12" rx="4" ry="9.5"/><path d="M2.5 12h19M4 7h16M4 17h16"/></g></svg>
        www.LodgeBridgely.net
      </li>
    </ul>
  </section>

</main>
</body>
</html>
```